Tolvin Waste Website Design

Our new start-up needs a website design. We plan to help businesses find more sustainable ways to manage their waste. Our initial website aims to gather contact data from potential business customers and comprehensive information from waste facilities and waste transporters. We have a logo design (attached) which we would like included in the website design. I have also attached a number of pages that describe what information should appear on each page as well as a web design brief file that describes the look we are after.

```html
<!DOCTYPE html>
<html lang="en">
<head>
<meta charset="utf-8">
<title>Tolvin Waste</title>
<link rel="stylesheet" href="https://fonts.googleapis.com/css2?family=Josefin+Sans:wght@300;400;600;700&display=swap">
<style>
:root{
  --lime:#a4cd39;
  --green:#6aa22b;
  --ink:#333333;
  --muted:#555555;
  --charcoal:#4a4a4a;
  --paper:#ffffff;
  --footer-bg:#f7f7f7;
  --line:#dddddd;
}
*{box-sizing:border-box;margin:0;padding:0}
html,body{width:783px;height:1200px;overflow:hidden}
body{font-family:"Josefin Sans",sans-serif;color:var(--ink);background:var(--paper);position:relative}
.site-header{position:absolute;top:0;left:0;width:783px;height:52px;background:var(--paper)}
.brand{position:absolute;left:102px;top:12px;display:flex;align-items:center;gap:6px}
.brand-dot{width:26px;height:26px;border-radius:50%;border:2px solid var(--lime)}
.brand-name{font-weight:600;font-size:15px;color:var(--ink);letter-spacing:.5px}
.main-nav{position:absolute;left:270px;top:22px;display:flex;gap:18px;align-items:center;font-size:7.5px;letter-spacing:1.2px;text-transform:uppercase}
.main-nav .home{width:8px;height:8px}
.header-phone{position:absolute;left:594px;top:19px;font-size:11px;letter-spacing:1px;display:flex;align-items:center;gap:6px}
.hero{position:absolute;top:52px;left:0;width:783px;height:314px;background:linear-gradient(180deg,#4f5a3c 0%,#3d4232 50%,#2c2e28 100%)}
.hero-inner{position:absolute;inset:0;text-align:center;color:var(--paper)}
.hero-kicker{position:absolute;top:89px;width:100%;font-size:17px;font-weight:300;letter-spacing:1px}
.hero-kicker b{color:var(--lime);font-weight:700}
.hero-title{position:absolute;top:114px;width:100%;font-size:29px;font-weight:300;letter-spacing:1.5px}
.hero-buttons{position:absolute;top:165px;width:100%;display:flex;justify-content:center;gap:6px}
.pill{height:27px;border-radius:14px;border:1.5px solid var(--paper);display:flex;align-items:center;justify-content:center;font-size:7px;font-weight:700;letter-spacing:1.5px;text-transform:uppercase;color:var(--paper)}
.pill.solid{background:var(--paper);color:var(--green)}
.services{position:absolute;top:366px;left:0;width:783px;height:194px;background:var(--lime);color:var(--paper);text-align:center}
.services h2{position:absolute;top:40px;width:100%;font-size:23px;font-weight:300;letter-spacing:1px}
.service{position:absolute;top:86px;width:180px;text-align:center}
.service svg{display:block;margin:0 auto 12px;height:44px}
.service span{font-size:10px;font-weight:700;letter-spacing:1px}
.service.active span{text-decoration:underline}
.about-photo{position:absolute;top:560px;left:0;width:391px;height:261px;background:linear-gradient(160deg,#b9c6d3 0%,#dfe3e6 45%,#8a8d8f 100%)}
.about{position:absolute;top:560px;left:391px;width:392px;height:261px;background:var(--paper)}
.about h2{position:absolute;left:42px;top:40px;font-size:23px;font-weight:300;letter-spacing:1px;color:var(--ink)}
.about p{position:absolute;left:42px;width:250px;font-size:8px;line-height:12.5px;color:var(--muted)}
.about .p1{top:79px}
.about .p2{top:142px}
.btn-outline{position:absolute;left:42px;top:197px;width:104px;height:21px;border:1px solid var(--green);border-radius:11px;font-size:6.5px;font-weight:700;letter-spacing:1.5px;color:var(--green);display:flex;align-items:center;justify-content:center}
.newsletter{position:absolute;top:821px;left:0;width:783px;height:138px;background:var(--charcoal);color:var(--paper)}
.newsletter h3{position:absolute;left:102px;top:42px;font-size:17px;font-weight:300;color:var(--lime)}
.newsletter p{position:absolute;left:102px;top:69px;width:230px;font-size:8px;line-height:11.5px}
.signup{position:absolute;left:400px;top:57px;width:281px;height:26px;background:var(--paper);border-radius:13px;border:1.5px solid var(--paper)}
.signup .placeholder{position:absolute;left:10px;top:9px;font-size:7.5px;color:#aaaaaa}
.signup .go{position:absolute;right:1px;top:1px;width:74px;height:21px;border-radius:11px;background:var(--green);color:var(--paper);font-size:6.5px;font-weight:700;letter-spacing:1.3px;display:flex;align-items:center;justify-content:center}
.site-footer{position:absolute;top:959px;left:0;width:783px;height:241px;background:var(--footer-bg);text-align:center}
.footer-mark{position:absolute;left:374px;top:35px;width:35px;height:35px;border-radius:50%;border:2px solid var(--lime)}
.contact-line{position:absolute;top:99px;width:100%;font-size:9.5px;letter-spacing:.5px}
.contact-line .label{color:var(--green)}
.footer-nav{position:absolute;left:151px;top:122px;width:481px;height:22px;border-top:1px solid var(--line);border-bottom:1px solid var(--line);display:flex;justify-content:center;align-items:center;gap:19px;font-size:6.8px;letter-spacing:1.3px;color:var(--muted)}
.to-top{position:absolute;left:697px;top:126px;width:15px;height:15px;border-radius:50%;background:var(--green)}
.social{position:absolute;top:164px;width:100%;display:flex;justify-content:center;gap:5px}
.social span{width:21px;height:21px;border-radius:50%;border:1px solid var(--green)}
.social span.on{background:var(--green)}
.copyright{position:absolute;top:206px;width:100%;font-size:7px;color:var(--muted)}
.copyright b{color:var(--green)}
</style>
</head>
<body>
<header class="site-header">
  <div class="brand"><div class="brand-dot"></div><div class="brand-name">Tolvin Waste</div></div>
  <nav class="main-nav">
    <svg class="home" viewBox="0 0 10 10"><path d="M1 5 5 1 9 5H8V9H2V5Z" fill="#6aa22b"/></svg>
    <span>About Us</span><span>What We Do</span><span>Resources</span><span>Contact Us</span>
  </nav>
  <div class="header-phone">
    <svg width="9" height="9" viewBox="0 0 10 10"><path d="M2 1 4 3 3 4Q4 6 6 7L7 6 9 8 8 9Q4 9 1 2Z" fill="none" stroke="#6aa22b" stroke-width="1"/></svg>
    555-014-2290
  </div>
</header>

<section class="hero" role="img" aria-label="Photo of a refuse collection truck beside waste bins on a tree-lined street">
  <div class="hero-inner">
    <div class="hero-kicker">WELCOME TO <b>TOLVIN WASTE</b></div>
    <h1 class="hero-title">Take Control of Your Waste Here</h1>
    <div class="hero-buttons">
      <div class="pill" style="width:136px">Waste Producers</div>
      <div class="pill solid" style="width:126px">Waste Facilities</div>
      <div class="pill" style="width:125px">Waste Transporters</div>
    </div>
  </div>
</section>

<section class="services">
  <h2>What We Do</h2>
  <div class="service" style="left:103px">
    <svg viewBox="0 0 44 44" width="44"><g fill="#fff"><rect x="3" y="14" width="11" height="26"/><rect x="16" y="14" width="12" height="26"/><rect x="30" y="14" width="11" height="26"/><rect x="2" y="10" width="40" height="3"/><circle cx="22" cy="5" r="3"/></g></svg>
    <span>Waste Producers</span>
  </div>
  <div class="service active" style="left:301px">
    <svg viewBox="0 0 44 44" width="44"><g fill="#fff"><rect x="4" y="20" width="14" height="20"/><rect x="3" y="16" width="16" height="3"/><path d="M24 6 38 12 34 14 40 40 34 40 30 20 26 24Z"/></g></svg>
    <span>Waste Facilities</span>
  </div>
  <div class="service" style="left:500px">
    <svg viewBox="0 0 48 44" width="48"><g fill="#fff"><rect x="2" y="8" width="30" height="26" rx="2"/><path d="M34 16H42L46 24V34H34Z"/><circle cx="11" cy="37" r="5"/><circle cx="38" cy="37" r="5"/></g></svg>
    <span>Waste Transporters</span>
  </div>
</section>

<div class="about-photo" role="img" aria-label="Photo of a white refuse collection truck parked on a street"></div>
<section class="about">
  <h2>About Us</h2>
  <p class="p1">There are many variations of passages of Lorem Ipsum available, but the majority have suffered alteration in some form, by injected humour, or randomised words which don't look even slightly believable. If you are.</p>
  <p class="p2">Going to use a passage of Lorem Ipsum, you need to be sure there embarrassing hidden in the middle of text. All the Lorem Ipsum generators ...</p>
  <div class="btn-outline">DISCOVER MORE</div>
</section>

<section class="newsletter">
  <h3>Subscribe Newsletters</h3>
  <p>We are just getting started. Please register your email address to receive updates from us.</p>
  <div class="signup"><span class="placeholder">Enter Your Email ...</span><span class="go">SUBSCRIBE</span></div>
</section>

<footer class="site-footer">
  <div class="footer-mark"></div>
  <div class="contact-line"><span class="label">Call Us:</span> 555-014-2290, <span class="label">E.</span> info@tolvinwaste.com</div>
  <nav class="footer-nav"><span>ABOUT US</span><span>WHAT WE DO</span><span>RESOURCES</span><span>RESULTS</span><span>FINAL RESULTS</span><span>CONTACT US</span></nav>
  <div class="to-top"><svg width="15" height="15" viewBox="0 0 15 15"><path d="M4.5 9 7.5 5.5 10.5 9Z" fill="#fff"/></svg></div>
  <div class="social"><span></span><span class="on"></span><span></span><span></span></div>
  <div class="copyright">© 2018 <b>TOLVIN</b> WASTE. All Right Reserved</div>
</footer>
</body>
</html>
```